I need a label design to go on our jars of honey. Our company is called Quillbrook Honey Co. The type of honey is called Marram Glade Honey. The jars are 1kg. Attached is the label size. Left hand side needs to have nutritional info... as attached. Middle section is our company name, honey type, 1kg & Marlowe Cove, NZ. Right hand side needs to have info as per photo (raw honey etc). I would like to upload more pictures... but I’m unsure how to do this? Thanks, Noreen

Target Market(s)

Honey consumers... families

Industry/Entity Type

Food Production

Colors

Designer to choose colors to be used in the design.

Requirements
Must have
• Nutritional info as per upload
• Type of honey & company name as per upload
• 1kg
• Address
Nice to have
• Similar fonts to upload.
• Possibly background image... floral or beach... very faint though.

```html
<!DOCTYPE html>
<html lang="en">
<head>
<meta charset="utf-8">
<title>Marram Glade Honey – Jar Label</title>
<link rel="stylesheet" href="https://fonts.googleapis.com/css2?family=Parisienne&family=Shadows+Into+Light+Two&family=Arimo:wght@400;700&display=swap">
<style>
  :root {
    --paper: #ffffff;
    --peach: #e9b88f;
    --peach-soft: #fbeee3;
    --rose: #c0464e;
    --leaf-light: #dfe7c8;
    --leaf: #a9bf86;
    --leaf-deep: #7f9a5e;
    --blossom: #cf8fb8;
    --panel: rgba(255,255,255,0.86);
    --veil: rgba(255,255,255,0.55);
    --ink: #333333;
  }
  * { box-sizing: border-box; margin: 0; padding: 0; }
  html, body { width: 1200px; height: 1000px; overflow: hidden; background: var(--paper); }
  .canvas { position: relative; width: 1200px; height: 1000px; }

  .title-band {
    position: absolute; left: 205px; top: 55px; width: 810px; height: 120px;
    background: linear-gradient(90deg, rgba(251,238,227,0) 0%, var(--peach-soft) 20%, var(--peach-soft) 80%, rgba(251,238,227,0) 100%);
    display: flex; align-items: center; justify-content: center;
  }
  .title-band h1 {
    font-family: "Parisienne", cursive; font-weight: 400;
    font-size: 64px; color: var(--peach); letter-spacing: 1px;
  }

  .label {
    position: absolute; left: 50px; top: 330px; width: 1100px; height: 370px;
    overflow: hidden; border-radius: 2px;
  }
  .label-backdrop {
    position: absolute; inset: 0;
    background:
      radial-gradient(ellipse at 20% 30%, rgba(207,143,184,0.45), transparent 40%),
      radial-gradient(ellipse at 75% 25%, rgba(207,143,184,0.35), transparent 35%),
      radial-gradient(ellipse at 50% 80%, var(--leaf-deep), transparent 60%),
      linear-gradient(180deg, var(--leaf-light) 0%, var(--leaf) 55%, var(--leaf-deep) 100%);
    opacity: 0.8;
  }
  .label-backdrop::after { content: ""; position: absolute; inset: 0; background: rgba(255,255,255,0.35); }

  .nutrition {
    position: absolute; left: 24px; top: 10px; width: 262px; height: 350px;
    background: var(--panel); padding: 8px 10px; z-index: 2;
    font-family: "Arimo", sans-serif; font-size: 10px; color: var(--ink); line-height: 1.25;
  }
  .nutrition .intro { text-align: center; border-bottom: 1px solid #888; padding-bottom: 4px; }
  .nutrition h2 { font-size: 11px; font-weight: 700; margin-top: 4px; }
  .nutrition .serving { border-bottom: 1px solid #888; padding-bottom: 4px; }
  .nutrition table { width: 100%; border-collapse: collapse; margin-top: 2px; table-layout: fixed; }
  .nutrition col.nutrient { width: 44%; }
  .nutrition col.amount { width: 28%; }
  .nutrition th { font-weight: 400; font-size: 8px; text-align: left; padding: 3px 2px 3px 0; border-bottom: 1px solid #888; }
  .nutrition td { padding: 1px 0; white-space: nowrap; }
  .nutrition tr:last-child td { padding-bottom: 4px; border-bottom: 1px solid #888; }
  .nutrition .care { text-align: center; padding: 5px 0; border-bottom: 1px solid #888; }
  .nutrition .trace p { font-weight: 700; font-size: 9px; padding: 2px 0; }

  .brand-disc {
    position: absolute; left: 400px; top: 20px; width: 320px; height: 320px; border-radius: 50%;
    background: var(--veil);
  }
  .brand-name {
    position: absolute; left: 400px; top: 60px; width: 320px; text-align: center;
    font-family: "Shadows Into Light Two", cursive; font-size: 22px; line-height: 1.2;
    color: var(--rose); text-transform: uppercase; letter-spacing: 1px;
  }
  .title-ribbon {
    position: absolute; left: 330px; top: 150px; width: 460px; height: 80px;
    background: rgba(255,255,255,0.85); transform: rotate(-9deg);
    display: flex; align-items: center; justify-content: center;
  }
  .title-ribbon span {
    font-family: "Parisienne", cursive; font-size: 38px; color: var(--peach); white-space: nowrap;
  }
  .place {
    position: absolute; left: 400px; top: 282px; width: 320px; text-align: center;
    font-family: "Shadows Into Light Two", cursive; font-size: 14px; letter-spacing: 2px;
    color: var(--peach); text-transform: uppercase;
  }
  .weight {
    position: absolute; left: 690px; top: 282px; width: 54px; height: 54px; border-radius: 50%;
    background: var(--veil); display: flex; align-items: center; justify-content: center;
    font-family: "Shadows Into Light Two", cursive; font-size: 20px; color: var(--rose);
  }

  .story {
    position: absolute; left: 820px; top: 14px; width: 262px; height: 340px; z-index: 2;
    background: var(--panel); padding: 20px 14px; text-align: center;
    font-family: "Shadows Into Light Two", cursive; font-size: 11.5px; line-height: 1.45;
    color: var(--rose); text-transform: uppercase; letter-spacing: 0.6px;
  }
  .story p + p { margin-top: 12px; }
</style>
</head>
<body>
<main class="canvas">
  <header class="title-band"><h1>Marram Glade Honey</h1></header>

  <section class="label">
    <div class="label-backdrop" role="img" aria-label="Faint photograph of a flowering coastal shrub with pink blossoms and green leaves, with a soft polka-dot band along the top"></div>

    <article class="nutrition">
      <div class="intro">100% New Zealand Honey<br>No added ingredients</div>
      <h2>NUTRITIONAL INFORMATION</h2>
      <div class="serving">Serving per package: 100<br>Serving size: 10g</div>
      <table>
        <colgroup><col class="nutrient"><col class="amount"><col class="amount"></colgroup>
        <tr><th></th><th>Average Quantity per Serving</th><th>Average Quantity per 100g</th></tr>
        <tr><td>Energy</td><td>134kj</td><td>1340kj</td></tr>
        <tr><td>Protein</td><td>0.04g</td><td>0.4g</td></tr>
        <tr><td>Fat total</td><td>0g</td><td>0g</td></tr>
        <tr><td>- saturated</td><td>0g</td><td>0g</td></tr>
        <tr><td>Carbohydrate</td><td>7.9g</td><td>79.6g</td></tr>
        <tr><td>- sugars</td><td>7.8g</td><td>78.1g</td></tr>
        <tr><td>Sodium</td><td>1.2mg</td><td>12mg</td></tr>
      </table>
      <div class="care">Store upright in a cool, dry place<br>No refrigeration needed.<br>Not recommended for infants below the age of 12 months</div>
      <div class="trace">
        <p>BEST BEFORE :</p>
        <p>RMP :</p>
        <p>BATCH No. :</p>
      </div>
    </article>

    <div class="brand-disc"></div>
    <div class="brand-name">Quillbrook<br>Honey Co.</div>
    <div class="title-ribbon"><span>Marram Glade Honey</span></div>
    <div class="place">Marlowe Cove, NZ</div>
    <div class="weight">1kg</div>

    <article class="story">
      <p>Sourced from the beautiful<br>Saltmere Peninsula</p>
      <p>Our honey comes to you raw and unpasteurised, ensuring it retains all the natural goodness!</p>
      <p>Arohanui<br>Alden, Noreen and boys</p>
      <p>Quillbrook – all thanks to God<br>for his incredible creation!</p>
      <p>www.quillbrookhoney.co.nz<br>42 Tidewell St<br>Marlowe Cove<br>New Zealand</p>
    </article>
  </section>
</main>
</body>
</html>
```